Business Profile Landing Page for search engine Start UP " Amber Quill"

Hi there
Amber Quill is an search engine for the Amber Quill - business.

What i´m looking for is a stunning singel Profile Landing Page for the Companys presentation.

Following Details should be included.

1st section
Comapanys name
Adress
info row ( opening time or what ever)
Profile Picture Big ( Could be the logo)
+3 smaller Pictures ( Maybe the store, main product ...)

2nd Section
navigation Icons for:
Call, Mail , Web, Route, Data

3er Section
About us.

Text lines.....
+Pictures slider

4th Section
1 row : Products ( Titel , Picture, Price)
2nd row :Service ( same as Products + text lines )

5th section
Blog Posts row

.....................................................
Well thats all, Colors used from the logo, u can also use the favicon somewhere (the crown magnifying glass)

Target Market(s)

All Comapnys, it should be an " used for all" design

Number of Pages Required

1 page

Requirements
Must have
• The first sighting is the important part, so the " first section should be impressively and makes the customers curious about more informations (very important for mobile version)
Nice to have
• If you can insert our favicon somewhere would be cool, but its not nessesery
Should not have
• you dont need to make a header or footer, that part is already done. i just need the main section design

```html
<!DOCTYPE html>
<html lang="en">
<head>
<meta charset="utf-8">
<title>Amber Quill – Business Profile</title>
<link href="https://fonts.googleapis.com/css2?family=Rubik:wght@400;500;700&family=Barlow+Condensed:wght@600;700&display=swap" rel="stylesheet">
<style>
:root{
  --gold:#cc8e0f;
  --gold-dark:#b77c08;
  --ink:#111;
  --text:#333;
  --muted:#555;
  --light:#ececec;
  --line:#d8d8d8;
  --ph:#b4b4b4;
  --dark:#2f2f2f;
  --white:#fff;
}
*{box-sizing:border-box;margin:0;padding:0}
html,body{width:1200px;height:3731px;overflow:hidden;background:var(--white)}
body{font-family:"Rubik",sans-serif;color:var(--text)}
.canvas{position:relative;width:1200px;height:3731px;overflow:hidden}
.abs{position:absolute}
.top-bar{left:0;top:0;width:1200px;height:13px;background:var(--gold)}

/* header */
.brand{font-family:"Rubik",sans-serif;font-weight:700;color:var(--gold);font-size:48px;line-height:1;letter-spacing:-0.5px}
.brand-sub{font-size:28px;color:var(--ink);font-weight:400}
.head-icon{width:46px;height:46px;border-radius:50%;background:var(--gold);display:flex;align-items:center;justify-content:center}
.head-label{color:var(--gold);font-size:16px;font-weight:500}
.head-text{font-size:17px;color:var(--text);line-height:21px}
.head-phone{font-size:31px;font-weight:500;color:var(--ink)}
.rule{height:1px;background:var(--line)}

/* info rows */
.info-row{height:48px;border:2px solid #cfcfcf;background:linear-gradient(#fdfdfd,#ececec);display:flex;align-items:center;padding-left:22px;font-weight:500;font-size:18px;color:var(--ink)}
.info-row .plus{position:absolute;right:0;top:0;width:46px;height:44px;background:var(--gold);color:#fff;display:flex;align-items:center;justify-content:center;font-size:16px}
.profile-box{height:272px;border:2px solid #cfcfcf;background:linear-gradient(#fff,#e8e8e8);display:flex;align-items:center;justify-content:center}
.profile-img{width:196px;height:196px;border-radius:50%;background:radial-gradient(circle,#2a2a2a 55%,#111 70%);border:5px solid var(--gold)}

/* nav icons */
.nav-item{width:160px;text-align:center}
.nav-circle{width:126px;height:126px;margin:0 auto;border-radius:50%;border:2px solid #cfcfcf;background:linear-gradient(#fff,#e6e6e6);display:flex;align-items:center;justify-content:center}
.nav-label{margin-top:20px;font-size:22px;font-weight:500;color:var(--ink)}

/* about */
.about{left:0;top:826px;width:1200px;height:594px;background:var(--gold)}
.about-frame{left:236px;top:84px;width:860px;height:416px;border:3px solid #fff;border-left:none}
.about-frame-l1{left:236px;top:84px;width:3px;height:22px;background:#fff}
.about-frame-l2{left:236px;top:480px;width:3px;height:22px;background:#fff}
.about-photo{left:517px;top:104px;width:561px;height:378px;background:linear-gradient(135deg,#e9eaec 0%,#c7cad0 30%,#2d3443 48%,#26304a 60%,#dfe1e4 100%)}
.about h2{left:98px;top:160px;font-size:44px;font-weight:700;color:#fff}
.about h3{left:98px;top:214px;font-size:20px;font-weight:500;color:#fff;letter-spacing:.5px}
.about p{left:98px;top:254px;width:345px;font-size:13.5px;line-height:17px;color:#fff}
.btn-dark{background:var(--ink);color:#fff;font-size:12px;font-weight:500;display:flex;align-items:center;justify-content:center}
.slider-dots{left:972px;top:458px;display:flex;gap:8px}
.slider-dots span{width:10px;height:10px;border:2px solid var(--ink)}
.slider-dots span.on{background:var(--gold-dark);border-color:var(--gold-dark)}

/* section headings */
.sec-mark{width:26px;height:26px;border-radius:50%;border:4px solid var(--gold);left:587px}
.sec-title{left:0;width:1200px;display:flex;align-items:center;justify-content:center;gap:14px;font-family:"Barlow Condensed",sans-serif;font-weight:700;font-size:42px;color:var(--gold);letter-spacing:.5px}
.sec-title .arrow{width:52px;height:10px}

.col{width:290px;text-align:center}
.col h4{font-family:"Rubik",sans-serif;font-size:21px;font-weight:500;color:var(--gold);margin-top:22px;letter-spacing:.3px}
.col p{font-size:13px;line-height:18px;color:var(--muted);margin:14px auto 0;width:270px}
.price{width:138px;height:32px;margin:16px auto 0;background:var(--ink);color:var(--gold);font-weight:700;font-size:20px;display:flex;align-items:center;justify-content:center}
.read-more{width:138px;height:32px;margin:16px auto 0;font-size:12px}
.ph-circle{display:block;margin:0 auto}

/* blog */
.blog{left:0;top:2665px;width:1200px;height:720px;background:var(--dark)}
.card{width:313px;height:465px;top:167px;overflow:hidden}
.card-body{padding:28px 30px 0;height:266px;position:relative}
.card-body h5{font-family:"Rubik",sans-serif;font-size:26px;font-weight:700;color:var(--gold)}
.card-body .bar{width:58px;height:3px;background:var(--gold);margin-top:16px}
.card-body .date{display:flex;align-items:center;gap:8px;margin-top:18px;font-size:14px;font-weight:500;color:var(--ink)}
.card-body p{margin-top:16px;font-size:13.5px;line-height:17px;color:var(--muted)}
.card-body .go{position:absolute;right:22px;bottom:14px}
.card.feature .card-body{background:var(--gold);height:265px}
.card.feature h5,.card.feature .date,.card.feature p{color:#fff}
.card.feature .bar{background:#fff}
.ph-rect{display:block;background:var(--ph)}
.blog-dots{left:558px;top:666px;display:flex;gap:9px}
.blog-dots span{width:12px;height:12px;border-radius:50%;background:#fff}
.blog-dots span.on{background:transparent;border:2px solid var(--gold)}

/* footer */
.foot-line{left:0;top:3544px;width:1200px;text-align:center;font-size:18px;color:var(--ink)}
.foot-line b{font-weight:400;color:var(--gold)}
.social{top:3600px;width:52px;height:52px;border-radius:50%;background:var(--gold)}
.copy{left:0;top:3692px;width:1200px;text-align:center;font-size:13px;color:var(--ink)}
</style>
</head>
<body>
<div class="canvas">
  <div class="abs top-bar"></div>

  <!-- header -->
  <div class="abs" style="left:97px;top:44px">
    <div class="brand">Amber Quill</div>
    <div class="brand-sub" style="margin-top:10px">Search &amp; Directory</div>
  </div>

  <div class="abs head-icon" style="left:424px;top:74px">
    <svg width="22" height="28" viewBox="0 0 22 28"><path d="M11 1C5.5 1 1.5 5 1.5 10.3 1.5 17 11 27 11 27s9.5-10 9.5-16.7C20.5 5 16.5 1 11 1z" fill="#fff"/><circle cx="11" cy="10.3" r="3.8" fill="#cc8e0f"/></svg>
  </div>
  <div class="abs" style="left:498px;top:58px">
    <div class="head-label">Address</div>
    <div class="head-text">Millbrook, OR 97042, USA</div>
    <div class="head-text">Lorem Ipsum is simply dummy</div>
  </div>

  <div class="abs head-icon" style="left:798px;top:74px">
    <svg width="24" height="24" viewBox="0 0 24 24"><path d="M6.6 10.8a15 15 0 0 0 6.6 6.6l2.2-2.2c.3-.3.7-.4 1-.2 1.1.4 2.3.6 3.6.6.6 0 1 .4 1 1V20c0 .6-.4 1-1 1A17 17 0 0 1 3 4c0-.6.4-1 1-1h3.5c.6 0 1 .4 1 1 0 1.3.2 2.5.6 3.6.1.3 0 .7-.2 1z" fill="#fff"/></svg>
  </div>
  <div class="abs" style="left:860px;top:56px">
    <div class="head-label">Call Us Today</div>
    <div class="head-phone">(123) 456-7890</div>
  </div>

  <div class="abs rule" style="left:98px;top:163px;width:1004px"></div>

  <!-- info rows -->
  <div class="abs info-row" style="left:98px;top:189px;width:326px">INFO ROW ONE<span class="plus">+</span></div>
  <div class="abs info-row" style="left:436px;top:189px;width:326px">INFO ROW TWO<span class="plus">+</span></div>
  <div class="abs info-row" style="left:775px;top:189px;width:326px">INFO ROW THREE<span class="plus">+</span></div>

  <div class="abs profile-box" style="left:98px;top:263px;width:326px"><div class="profile-img" role="img" aria-label="Company profile picture"></div></div>
  <div class="abs profile-box" style="left:436px;top:263px;width:326px"><div class="profile-img" role="img" aria-label="Store picture"></div></div>
  <div class="abs profile-box" style="left:775px;top:263px;width:326px"><div class="profile-img" role="img" aria-label="Main product picture"></div></div>

  <div class="abs rule" style="left:98px;top:574px;width:1004px"></div>

  <!-- navigation icons -->
  <div class="abs nav-item" style="left:80px;top:604px">
    <div class="nav-circle"><svg width="60" height="60" viewBox="0 0 24 24"><path d="M6.6 10.8a15 15 0 0 0 6.6 6.6l2.2-2.2c.3-.3.7-.4 1-.2 1.1.4 2.3.6 3.6.6.6 0 1 .4 1 1V20c0 .6-.4 1-1 1A17 17 0 0 1 3 4c0-.6.4-1 1-1h3.5c.6 0 1 .4 1 1 0 1.3.2 2.5.6 3.6.1.3 0 .7-.2 1z" fill="#cc8e0f"/><path d="M14 3.5a7 7 0 0 1 6.5 6.5M14 6.5a4 4 0 0 1 3.5 3.5" stroke="#cc8e0f" stroke-width="1.6" fill="none" stroke-linecap="round"/></svg></div>
    <div class="nav-label">CALL</div>
  </div>
  <div class="abs nav-item" style="left:302px;top:604px">
    <div class="nav-circle"><svg width="62" height="44" viewBox="0 0 62 44"><rect x="1" y="1" width="60" height="42" fill="#cc8e0f"/><path d="M2 3l29 22 29-22M2 41l21-19M60 41L39 22" stroke="#fff" stroke-width="2.5" fill="none"/></svg></div>
    <div class="nav-label">MAIL</div>
  </div>
  <div class="abs nav-item" style="left:518px;top:604px">
    <div class="nav-circle"><svg width="62" height="62" viewBox="0 0 62 62"><circle cx="31" cy="31" r="29" fill="#cc8e0f"/><g stroke="#fff" stroke-width="2.5" fill="none"><ellipse cx="31" cy="31" rx="12" ry="29"/><path d="M31 2v58M2 31h58M6 17h50M6 45h50"/></g></svg></div>
    <div class="nav-label">WEB</div>
  </div>
  <div class="abs nav-item" style="left:744px;top:604px">
    <div class="nav-circle"><svg width="70" height="56" viewBox="0 0 70 56"><path d="M15 2C8 2 3 7 3 14c0 9 12 22 12 22s12-13 12-22C27 7 22 2 15 2z" fill="#cc8e0f"/><circle cx="15" cy="14" r="5" fill="#fff"/><path d="M56 2c-6 0-10 4-10 10 0 8 10 18 10 18s10-10 10-18c0-6-4-10-10-10z" fill="#cc8e0f"/><circle cx="56" cy="12" r="4" fill="#fff"/><path d="M15 42l5 12h18l6-14h12" stroke="#cc8e0f" stroke-width="4" fill="none" stroke-linejoin="round"/></svg></div>
    <div class="nav-label">ROUTE</div>
  </div>
  <div class="abs nav-item" style="left:956px;top:604px">
    <div class="nav-circle"><svg width="66" height="62" viewBox="0 0 66 62"><g fill="#cc8e0f"><ellipse cx="26" cy="9" rx="24" ry="8"/><path d="M2 14c0 5 11 8 24 8s24-3 24-8v9c0 5-11 8-24 8S2 28 2 23z"/><path d="M2 29c0 5 11 8 24 8 3 0 6 0 9-1v9c-3 1-6 1-9 1-13 0-24-3-24-8z"/><path d="M2 44c0 5 11 8 24 8h7v8h-7C13 60 2 57 2 52z"/><circle cx="51" cy="47" r="10"/></g><circle cx="51" cy="47" r="4" fill="#fff"/><g stroke="#cc8e0f" stroke-width="4"><path d="M51 33v28M37 47h28M41 37l20 20M61 37L41 57"/></g><circle cx="51" cy="47" r="4" fill="#fff"/></svg></div>
    <div class="nav-label">DATA</div>
  </div>

  <!-- about -->
  <section class="abs about">
    <div class="abs about-frame"></div>
    <div class="abs about-frame-l1"></div>
    <div class="abs about-frame-l2"></div>
    <h2 class="abs">ABOUT</h2>
    <h3 class="abs">TRANSFORMING BRANDS</h3>
    <p class="abs">Lorem Ipsum is simply dummy text of the printing and typesetting industry. Lorem Ipsum has been the industry's standard dummy text ever since the 1500s, when an unknown printer took a galley of type and scrambled it to make a type specimen book. It has survived not only five centuries, but also the leap into electronic typesetting, remaining essentially unchanged.</p>
    <div class="abs btn-dark" style="left:98px;top:400px;width:136px;height:39px">GET IN TOUCH</div>
    <div class="abs about-photo" role="img" aria-label="Slider photo: businessman in a suit holding a glowing consulting concept diagram"></div>
    <div class="abs slider-dots"><span class="on"></span><span></span><span></span><span></span><span></span></div>
  </section>

  <!-- products -->
  <section class="abs" style="left:0;top:1420px;width:1200px;height:635px;background:var(--light)">
    <div class="abs sec-mark" style="top:42px"></div>
    <div class="abs sec-title" style="top:80px">
      <svg class="arrow" viewBox="0 0 52 10"><path d="M0 5h44M0 5l6-4M0 5l6 4" stroke="#cc8e0f" stroke-width="2" fill="none"/><circle cx="47" cy="5" r="3" stroke="#cc8e0f" stroke-width="2" fill="none"/></svg>
      <span>OUR PRODUCTS</span>
      <svg class="arrow" viewBox="0 0 52 10"><circle cx="5" cy="5" r="3" stroke="#cc8e0f" stroke-width="2" fill="none"/><path d="M8 5h44M52 5l-6-4M52 5l-6 4" stroke="#cc8e0f" stroke-width="2" fill="none"/></svg>
    </div>

    <div class="abs col" style="left:122px;top:160px">
      <svg class="ph-circle" width="212" height="212" viewBox="0 0 212 212" role="img" aria-label="Product image"><circle cx="106" cy="106" r="103" fill="#b4b4b4" stroke="#cc8e0f" stroke-width="3"/><path d="M34 34l144 144M178 34L34 178" stroke="#fff" stroke-width="2"/><rect x="26" y="92" width="160" height="28" fill="#b4b4b4"/><text x="106" y="115" text-anchor="middle" font-family="Rubik,sans-serif" font-size="23" font-weight="500" fill="#fff">PLACEHOLDER</text></svg>
      <h4>PRODUCT TITLE</h4>
      <p>Lorem Ipsum is simply dummy text of the printing and typesetting industry. Lorem Ipsum has been the industry's standard dummy text ever since the 1500s book.</p>
      <div class="price">$ 20.00</div>
    </div>
    <div class="abs col" style="left:453px;top:160px">
      <svg class="ph-circle" width="212" height="212" viewBox="0 0 212 212" role="img" aria-label="Product image"><circle cx="106" cy="106" r="103" fill="#b4b4b4" stroke="#cc8e0f" stroke-width="3"/><path d="M34 34l144 144M178 34L34 178" stroke="#fff" stroke-width="2"/><rect x="26" y="92" width="160" height="28" fill="#b4b4b4"/><text x="106" y="115" text-anchor="middle" font-family="Rubik,sans-serif" font-size="23" font-weight="500" fill="#fff">PLACEHOLDER</text></svg>
      <h4>PRODUCT TITLE</h4>
      <p>Lorem Ipsum is simply dummy text of the printing and typesetting industry. Lorem Ipsum has been the industry's standard dummy text ever since the 1500s book.</p>
      <div class="price">$ 20.00</div>
    </div>
    <div class="abs col" style="left:788px;top:160px">
      <svg class="ph-circle" width="212" height="212" viewBox="0 0 212 212" role="img" aria-label="Product image"><circle cx="106" cy="106" r="103" fill="#b4b4b4" stroke="#cc8e0f" stroke-width="3"/><path d="M34 34l144 144M178 34L34 178" stroke="#fff" stroke-width="2"/><rect x="26" y="92" width="160" height="28" fill="#b4b4b4"/><text x="106" y="115" text-anchor="middle" font-family="Rubik,sans-serif" font-size="23" font-weight="500" fill="#fff">PLACEHOLDER</text></svg>
      <h4>PRODUCT TITLE</h4>
      <p>Lorem Ipsum is simply dummy text of the printing and typesetting industry. Lorem Ipsum has been the industry's standard dummy text ever since the 1500s book.</p>
      <div class="price">$ 20.00</div>
    </div>
  </section>

  <!-- services -->
  <section class="abs" style="left:0;top:2055px;width:1200px;height:610px;background:var(--white)">
    <div class="abs sec-mark" style="top:32px"></div>
    <div class="abs sec-title" style="top:82px">
      <svg class="arrow" viewBox="0 0 52 10"><path d="M0 5h44M0 5l6-4M0 5l6 4" stroke="#cc8e0f" stroke-width="2" fill="none"/><circle cx="47" cy="5" r="3" stroke="#cc8e0f" stroke-width="2" fill="none"/></svg>
      <span>OUR SERVICES</span>
      <svg class="arrow" viewBox="0 0 52 10"><circle cx="5" cy="5" r="3" stroke="#cc8e0f" stroke-width="2" fill="none"/><path d="M8 5h44M52 5l-6-4M52 5l-6 4" stroke="#cc8e0f" stroke-width="2" fill="none"/></svg>
    </div>

    <div class="abs col" style="left:122px;top:158px">
      <svg class="ph-circle" width="212" height="212" viewBox="0 0 212 212" role="img" aria-label="Service image"><circle cx="106" cy="106" r="103" fill="#b4b4b4" stroke="#cc8e0f" stroke-width="3"/><path d="M34 34l144 144M178 34L34 178" stroke="#fff" stroke-width="2"/><rect x="26" y="92" width="160" height="28" fill="#b4b4b4"/><text x="106" y="115" text-anchor="middle" font-family="Rubik,sans-serif" font-size="23" font-weight="500" fill="#fff">PLACEHOLDER</text></svg>
      <h4>SERVICE ONE</h4>
      <p>Lorem Ipsum is simply dummy text of the printing and typesetting industry. Lorem Ipsum has been the industry's standard dummy text ever since the 1500s book.</p>
      <div class="btn-dark read-more">READ MORE</div>
    </div>
    <div class="abs col" style="left:453px;top:158px">
      <svg class="ph-circle" width="212" height="212" viewBox="0 0 212 212" role="img" aria-label="Service image"><circle cx="106" cy="106" r="103" fill="#b4b4b4" stroke="#cc8e0f" stroke-width="3"/><path d="M34 34l144 144M178 34L34 178" stroke="#fff" stroke-width="2"/><rect x="26" y="92" width="160" height="28" fill="#b4b4b4"/><text x="106" y="115" text-anchor="middle" font-family="Rubik,sans-serif" font-size="23" font-weight="500" fill="#fff">PLACEHOLDER</text></svg>
      <h4>SERVICE TWO</h4>
      <p>Lorem Ipsum is simply dummy text of the printing and typesetting industry. Lorem Ipsum has been the industry's standard dummy text ever since the 1500s book.</p>
      <div class="btn-dark read-more">READ MORE</div>
    </div>
    <div class="abs col" style="left:788px;top:158px">
      <svg class="ph-circle" width="212" height="212" viewBox="0 0 212 212" role="img" aria-label="Service image"><circle cx="106" cy="106" r="103" fill="#b4b4b4" stroke="#cc8e0f" stroke-width="3"/><path d="M34 34l144 144M178 34L34 178" stroke="#fff" stroke-width="2"/><rect x="26" y="92" width="160" height="28" fill="#b4b4b4"/><text x="106" y="115" text-anchor="middle" font-family="Rubik,sans-serif" font-size="23" font-weight="500" fill="#fff">PLACEHOLDER</text></svg>
      <h4>SERVICE THREE</h4>
      <p>Lorem Ipsum is simply dummy text of the printing and typesetting industry. Lorem Ipsum has been the industry's standard dummy text ever since the 1500s book.</p>
      <div class="btn-dark read-more">READ MORE</div>
    </div>
  </section>

  <!-- blog -->
  <section class="abs blog">
    <div class="abs sec-mark" style="top:40px"></div>
    <div class="abs sec-title" style="top:84px">
      <svg class="arrow" viewBox="0 0 52 10"><path d="M0 5h44M0 5l6-4M0 5l6 4" stroke="#fff" stroke-width="2" fill="none"/><circle cx="47" cy="5" r="3" stroke="#fff" stroke-width="2" fill="none"/></svg>
      <span>OUR BLOG</span>
      <svg class="arrow" viewBox="0 0 52 10"><circle cx="5" cy="5" r="3" stroke="#fff" stroke-width="2" fill="none"/><path d="M8 5h44M52 5l-6-4M52 5l-6 4" stroke="#fff" stroke-width="2" fill="none"/></svg>
    </div>

    <article class="abs card" style="left:104px;background:#fff">
      <div class="card-body">
        <h5>HEADING ONE</h5>
        <div class="bar"></div>
        <div class="date"><svg width="22" height="20" viewBox="0 0 22 20"><rect x="1" y="3" width="20" height="16" fill="none" stroke="#cc8e0f" stroke-width="1.6"/><path d="M1 7h20M6 1v4M16 1v4" stroke="#cc8e0f" stroke-width="1.6"/></svg>June 23, 2020</div>
        <p>Lorem Ipsum is simply dummy text of the printing and typesetting industry. Lorem Ipsum has been the industry's standard dummy text ever since the 1500s, when an unknown printer.</p>
        <svg class="go" width="26" height="18" viewBox="0 0 26 18"><path d="M1 9h22M15 1l8 8-8 8" stroke="#cc8e0f" stroke-width="2.5" fill="none"/></svg>
      </div>
      <svg class="ph-rect" width="313" height="199" viewBox="0 0 313 199" role="img" aria-label="Blog post image"><rect width="313" height="199" fill="#b4b4b4"/><path d="M60 0l193 199M253 0L60 199" stroke="#fff" stroke-width="2"/><rect x="40" y="82" width="233" height="34" fill="#b4b4b4"/><text x="156" y="110" text-anchor="middle" font-family="Rubik,sans-serif" font-size="30" font-weight="500" fill="#fff">PLACEHOLDER</text></svg>
    </article>

    <article class="abs card feature" style="left:446px">
      <svg class="ph-rect" width="313" height="200" viewBox="0 0 313 200" role="img" aria-label="Blog post image"><rect width="313" height="200" fill="#b4b4b4"/><path d="M60 0l193 200M253 0L60 200" stroke="#fff" stroke-width="2"/><rect x="40" y="82" width="233" height="34" fill="#b4b4b4"/><text x="156" y="110" text-anchor="middle" font-family="Rubik,sans-serif" font-size="30" font-weight="500" fill="#fff">PLACEHOLDER</text></svg>
      <div class="card-body">
        <h5>HEADING TWO</h5>
        <div class="bar"></div>
        <div class="date"><svg width="22" height="20" viewBox="0 0 22 20"><rect x="1" y="3" width="20" height="16" fill="none" stroke="#fff" stroke-width="1.6"/><path d="M1 7h20M6 1v4M16 1v4" stroke="#fff" stroke-width="1.6"/></svg>June 23, 2020</div>
        <p>Lorem Ipsum is simply dummy text of the printing and typesetting industry. Lorem Ipsum has been the industry's standard dummy text ever since the 1500s, when an unknown printer.</p>
        <svg class="go" width="26" height="18" viewBox="0 0 26 18"><path d="M1 9h22M15 1l8 8-8 8" stroke="#fff" stroke-width="2.5" fill="none"/></svg>
      </div>
    </article>

    <article class="abs card" style="left:784px;background:#fff">
      <div class="card-body">
        <h5>HEADING THREE</h5>
        <div class="bar"></div>
        <div class="date"><svg width="22" height="20" viewBox="0 0 22 20"><rect x="1" y="3" width="20" height="16" fill="none" stroke="#cc8e0f" stroke-width="1.6"/><path d="M1 7h20M6 1v4M16 1v4" stroke="#cc8e0f" stroke-width="1.6"/></svg>June 23, 2020</div>
        <p>Lorem Ipsum is simply dummy text of the printing and typesetting industry. Lorem Ipsum has been the industry's standard dummy text ever since the 1500s, when an unknown printer.</p>
        <svg class="go" width="26" height="18" viewBox="0 0 26 18"><path d="M1 9h22M15 1l8 8-8 8" stroke="#cc8e0f" stroke-width="2.5" fill="none"/></svg>
      </div>
      <svg class="ph-rect" width="313" height="199" viewBox="0 0 313 199" role="img" aria-label="Blog post image"><rect width="313" height="199" fill="#b4b4b4"/><path d="M60 0l193 199M253 0L60 199" stroke="#fff" stroke-width="2"/><rect x="40" y="82" width="233" height="34" fill="#b4b4b4"/><text x="156" y="110" text-anchor="middle" font-family="Rubik,sans-serif" font-size="30" font-weight="500" fill="#fff">PLACEHOLDER</text></svg>
    </article>

    <div class="abs blog-dots"><span class="on"></span><span></span><span></span><span></span></div>
  </section>

  <!-- footer -->
  <div class="abs" style="left:0;top:3428px;width:1200px;text-align:center">
    <div class="brand">Amber Quill</div>
    <div class="brand-sub" style="margin-top:10px">Search &amp; Directory</div>
  </div>
  <div class="abs foot-line"><b>Address:</b> Millbrook, OR 97042, USA &nbsp;|&nbsp; <b>Phone:</b> (123) 456-7890 &nbsp;|&nbsp; <b>Email:</b> info@emailaddress.com</div>
  <div class="abs social" style="left:429px" role="img" aria-label="Social link"></div>
  <div class="abs social" style="left:503px" role="img" aria-label="Social link"></div>
  <div class="abs social" style="left:577px" role="img" aria-label="Social link"></div>
  <div class="abs social" style="left:658px" role="img" aria-label="Social link"></div>
  <div class="abs social" style="left:733px" role="img" aria-label="Social link"></div>
  <div class="abs copy">Amber Quill &nbsp;|&nbsp; All Rights Reserved &nbsp;© 2020</div>
</div>
</body>
</html>
```